TotBramble Needs a Banner Ad Design

We need a banner ad design for a new competition and will be placed on Circlehub and at our website (totbramble.example).

Competition name: Support your community

How it works?
Any person can nominate a kids business from their local community to win free advertising at TotBramble for 2 months. The person that nominates the winning business will win a $100 TotBramble ValuePass.
To nominate a business the person needs only to write the business name and location on the Circlehub post comments.

The look and feel of the banner:
Clean but at the same time communicate the message effectively

Reason: Given my unavailability to provide immediate feedback, I am keen to extend the deadline so we have a bit more time to work on the banners. Cheers!

```html
<!DOCTYPE html>
<html lang="en">
<head>
<meta charset="utf-8">
<title>Support your community – TotBramble</title>
<link rel="stylesheet" href="https://fonts.googleapis.com/css2?family=Titan+One&family=Fredoka:wght@600&family=Arimo:ital,wght@0,400;1,700&display=swap">
<style>
  :root {
    --paper: #ffffff;
    --coral: #f06a76;
    --coral-deep: #e35866;
    --sky: #1c9be0;
    --sky-deep: #0a5f9c;
    --teal: #3a8d9c;
    --teal-shadow: #245f6b;
    --ink: #1d1d1d;
    --alert-red: #ea1c1c;
    --band: #1e1e1e;
    --band-text: #b4cdf4;
    --silver-light: #fafafa;
    --silver-dark: #9c9c9c;
  }
  * { margin: 0; padding: 0; box-sizing: border-box; }
  html, body { width: 1200px; height: 524px; overflow: hidden; background: var(--paper); }

  .banner {
    position: relative;
    width: 1200px;
    height: 524px;
    overflow: hidden;
    background: var(--paper);
  }

  .hands-photo {
    position: absolute;
    inset: 0;
    clip-path: polygon(0 0, 500px 0, 365px 524px, 0 524px);
    background:
      radial-gradient(ellipse at 35% 55%, #c98f6e 0%, #b07658 35%, transparent 70%),
      linear-gradient(135deg, #e9c7b0 0%, #c48966 45%, #8f5a3f 100%);
  }

  .coral-panel {
    position: absolute;
    inset: 0;
    clip-path: polygon(498px 0, 1200px 0, 1200px 432px, 383px 432px);
    background: linear-gradient(160deg, var(--coral) 0%, var(--coral-deep) 100%);
  }

  .info-band {
    position: absolute;
    inset: 0;
    clip-path: polygon(362px 432px, 1200px 432px, 1200px 524px, 352px 524px);
    background: var(--band);
  }
  .info-band p {
    position: absolute;
    left: 380px;
    right: 0;
    top: 440px;
    text-align: center;
    font-family: "Arimo", Arial, sans-serif;
    font-size: 22px;
    line-height: 36px;
    color: var(--band-text);
  }

  .title-pill {
    position: absolute;
    left: 548px;
    top: 8px;
    width: 644px;
    height: 66px;
    border-radius: 33px;
    background: var(--sky);
    box-shadow: 0 3px 0 var(--sky-deep);
    display: flex;
    align-items: center;
    justify-content: center;
  }
  .title-pill h1 {
    font-family: "Titan One", "Cooper Black", serif;
    font-weight: 400;
    font-size: 41px;
    line-height: 1;
    margin-top: -4px;
    color: var(--paper);
    -webkit-text-stroke: 2px var(--sky-deep);
    paint-order: stroke fill;
    white-space: nowrap;
  }

  .offer-box {
    position: absolute;
    inset: 0;
  }
  .offer-box svg { position: absolute; inset: 0; }
  .offer-text {
    position: absolute;
    left: 568px;
    top: 118px;
    width: 632px;
    transform: rotate(6deg);
    transform-origin: 50% 50%;
    text-align: center;
    font-family: "Fredoka", "Berlin Sans FB", sans-serif;
    font-weight: 600;
    font-size: 35px;
    line-height: 46px;
    letter-spacing: -0.3px;
    white-space: nowrap;
    color: var(--ink);
  }
  .offer-text .highlight { color: var(--alert-red); }

  .prize-badge {
    position: absolute;
    left: 335px;
    top: 162px;
    width: 214px;
    height: 214px;
    clip-path: polygon(100% 50%, 92.5% 56.7%, 97.6% 65.5%, 88.3% 69.5%, 90.5% 79.4%, 80.4% 80.4%, 79.4% 90.5%, 69.5% 88.3%, 65.5% 97.6%, 56.7% 92.5%, 50% 100%, 43.3% 92.5%, 34.5% 97.6%, 30.5% 88.3%, 20.6% 90.5%, 19.6% 80.4%, 9.5% 79.4%, 11.7% 69.5%, 2.4% 65.5%, 7.5% 56.7%, 0 50%, 7.5% 43.3%, 2.4% 34.5%, 11.7% 30.5%, 9.5% 20.6%, 19.6% 19.6%, 20.6% 9.5%, 30.5% 11.7%, 34.5% 2.4%, 43.3% 7.5%, 50% 0, 56.7% 7.5%, 65.5% 2.4%, 69.5% 11.7%, 79.4% 9.5%, 80.4% 19.6%, 90.5% 20.6%, 88.3% 30.5%, 97.6% 34.5%, 92.5% 43.3%);
    background: radial-gradient(circle at 40% 35%, var(--silver-light) 0%, #d6d6d6 55%, var(--silver-dark) 100%);
    display: flex;
    align-items: center;
    justify-content: center;
  }
  .prize-badge p {
    text-align: center;
    font-family: "Arimo", Arial, sans-serif;
    font-style: italic;
    font-weight: 700;
    font-size: 16px;
    line-height: 20px;
    white-space: nowrap;
    color: #3a3a3a;
  }
  .prize-badge .prize-amount { color: var(--alert-red); }
</style>
</head>
<body>
  <main class="banner">
    <div class="hands-photo" role="img" aria-label="Photo of many hands from different people clasped together in a circle"></div>

    <div class="coral-panel"></div>

    <div class="title-pill">
      <h1>Support your community</h1>
    </div>

    <div class="offer-box">
      <svg width="1200" height="524" viewBox="0 0 1200 524" aria-hidden="true">
        <polygon points="548,98 1200,112 1200,418 578,404" fill="var(--teal-shadow)"/>
        <polygon points="542,90 1200,104 1200,408 570,394" fill="var(--teal)"/>
      </svg>
      <p class="offer-text">
        Nominate a kids business from your<br>
        local community and win <span class="highlight">FREE</span><br>
        advertising at<br>
        <span class="highlight">TotBramble</span> for <span class="highlight">2</span> months
      </p>
    </div>

    <div class="prize-badge">
      <p><span class="prize-amount">$100 GIFT</span><br><span class="prize-amount">CARD</span> to the person<br>who nominates the<br>winning kids<br>business</p>
    </div>

    <div class="info-band">
      <p>To nominate a kids business you only need to write the business<br>name and location on the Circlehub post comments</p>
    </div>
  </main>
</body>
</html>
```